Dale Harwick Terrain Services LLC

Need a business card design for a new company based in Cedar Bend, MS. We specialize in under-brush clearing, forestry mulching, cutover mulching, right of way clearing, land line & fence row clearing, bush hogging, land clearing, wildlife food plots. We use compact track loaders and tractors. I will attach a picture of a compact track loader I would like to have on the card design if possible.

Target Market(s)

Businesses / Land Owners

Contact Information for Business Card

Dale Harwick
Owner / Operator

Cedar Bend, MS

Call/Text: 601-555-3871
dhterrainwork@mailvista.test
FB: @daleharwickterrainservicesllc

Font styles to use
Serif
Sans Serif

Requirements
Must have
• Contact info, city & state. Description of services.
Nice to have
• Not overwhelming back ground but eye and interest catching with clear objection of the business

```html
<!DOCTYPE html>
<html lang="en">
<head>
<meta charset="utf-8">
<title>Dale Harwick Terrain Services LLC – Business Card</title>
<link rel="stylesheet" href="https://fonts.googleapis.com/css2?family=Open+Sans:wght@300;400;600;700;800&display=swap">
<style>
  :root {
    --backdrop: #1d1d1f;
    --card: #f7f7f5;
    --ink: #3b3b3b;
    --ink-soft: #555555;
    --accent: #f1c232;
    --photo-sky: #c9d8cf;
    --photo-trees: #34502c;
    --photo-grass: #8fae4e;
    --photo-machine: #d9a82a;
    --photo-forest-light: #c8b86a;
    --photo-forest-dark: #5b4a22;
  }
  * { box-sizing: border-box; margin: 0; padding: 0; }
  html, body {
    width: 1200px; height: 900px; overflow: hidden;
    background: var(--backdrop);
    font-family: "Open Sans", Arial, sans-serif;
    color: var(--ink);
  }
  .card {
    position: absolute; left: 290px;
    width: 620px; height: 354px;
    background: var(--card);
    overflow: hidden;
    box-shadow: 0 12px 30px rgba(0,0,0,.5);
  }
  .card--front { top: 70px; }
  .card--back { top: 476px; }

  .card__photo { position: absolute; top: 0; left: 0; height: 100%; }
  .card--front .card__photo {
    width: 430px;
    background: linear-gradient(180deg, var(--photo-sky) 0%, var(--photo-trees) 22%, var(--photo-trees) 45%, var(--photo-machine) 55%, var(--photo-grass) 80%, var(--photo-grass) 100%);
  }
  .card--back .card__photo {
    width: 330px;
    background: linear-gradient(160deg, var(--photo-forest-light) 0%, var(--photo-forest-dark) 35%, var(--photo-machine) 60%, var(--photo-forest-dark) 100%);
  }
  .card__photo::after {
    content: ""; position: absolute; inset: 0;
    background: linear-gradient(90deg, rgba(247,247,245,0) 45%, var(--card) 100%);
  }

  .card__info { position: absolute; }
  .card--front .card__info { left: 330px; top: 38px; }
  .card--back .card__info { left: 250px; top: 40px; }

  .company { font-size: 27px; line-height: 1.12; font-weight: 300; color: var(--ink); }
  .company strong { font-weight: 700; }
  .city { font-size: 22px; font-weight: 400; color: var(--accent); margin-top: 2px; }

  .person { margin-top: 16px; font-size: 28px; font-weight: 800; letter-spacing: .5px; text-transform: uppercase; line-height: 1; }
  .role { font-size: 17px; color: var(--accent); margin-top: 3px; }

  .contacts { list-style: none; margin-top: 14px; }
  .contacts li { display: flex; align-items: center; gap: 10px; font-size: 14px; color: var(--ink-soft); margin-bottom: 9px; }
  .contacts .icon { width: 20px; height: 20px; flex: none; }

  .services-title { margin-top: 18px; font-size: 19px; font-weight: 800; text-transform: uppercase; letter-spacing: .3px; }
  .services { list-style: none; margin-top: 6px; }
  .services li { font-size: 14px; font-weight: 700; text-transform: uppercase; color: var(--accent); line-height: 1.45; display: flex; align-items: center; gap: 8px; }
  .services li::before { content: ""; width: 6px; height: 6px; background: var(--ink); flex: none; }
</style>
</head>
<body>

<section class="card card--front">
  <div class="card__photo" role="img" aria-label="Photo of a yellow compact track loader with a mulching head on grass in front of trees"></div>
  <div class="card__info">
    <p class="company"><strong>Dale Harwick</strong> Terrain<br>Services LLC</p>
    <p class="city">Cedar Bend, MS</p>
    <p class="person">Dale Harwick</p>
    <p class="role">Owner / Operator</p>
    <ul class="contacts">
      <li>
        <svg class="icon" viewBox="0 0 20 20" aria-hidden="true"><circle cx="10" cy="10" r="10" fill="var(--accent)"/><path d="M7 5.5l2 2-1.2 1.3a6 6 0 0 0 3.4 3.4L12.5 11l2 2-1.3 1.5C9.5 14.3 5.7 10.5 5.5 6.8z" fill="#fff"/></svg>
        601-555-3871
      </li>
      <li>
        <svg class="icon" viewBox="0 0 20 20" aria-hidden="true"><circle cx="10" cy="10" r="10" fill="var(--accent)"/><rect x="5" y="6.5" width="10" height="7" rx="1" fill="#fff"/><path d="M5.5 7l4.5 3.5L14.5 7" stroke="var(--accent)" stroke-width="1.2" fill="none"/></svg>
        dhterrainwork@mailvista.test
      </li>
      <li>
        <svg class="icon" viewBox="0 0 20 20" aria-hidden="true"><circle cx="10" cy="10" r="10" fill="var(--accent)"/></svg>
        @daleharwickterrainservicesllc
      </li>
    </ul>
  </div>
</section>

<section class="card card--back">
  <div class="card__photo" role="img" aria-label="Photo of a yellow compact track loader clearing brush in a sunlit forest"></div>
  <div class="card__info">
    <p class="company"><strong>Dale Harwick</strong> Terrain<br>Services LLC</p>
    <p class="city">Cedar Bend, MS</p>
    <p class="services-title">We Specialize In</p>
    <ul class="services">
      <li>Under-Brush Clearing</li>
      <li>Forestry Mulching</li>
      <li>Right of Way Clearing</li>
      <li>Land Line &amp; Fence Row Clearing</li>
      <li>Bush Hogging</li>
      <li>Land Clearing</li>
      <li>Wildlife Food Plots</li>
    </ul>
  </div>
</section>

</body>
</html>
```